K&R Security Services PTY. LTD.

Ive just had my logo made and I'm looking for some simple but strong designs for my business cards the company is a security company.

Please use dark colors.

Regards,

Owen Deloit

Reason: Need more time for discussion with other directors

Industry/Entity Type

Security

Font styles to use
Sans Serif
Decorative

```html
<!DOCTYPE html>
<html lang="en">
<head>
<meta charset="utf-8">
<title>K&amp;R Security Services – Business Card</title>
<link rel="stylesheet" href="https://fonts.googleapis.com/css2?family=Cinzel:wght@400;600&family=Josefin+Sans:wght@300;400&display=swap">
<style>
  :root {
    --stage: #4b5457;
    --card-dark: #1c1c1c;
    --card-light: #ffffff;
    --ink: #1f1f1f;
    --ink-soft: #5c6163;
    --text-on-dark: #d4d4d4;
  }
  * { box-sizing: border-box; margin: 0; padding: 0; }
  html, body { width: 1200px; height: 741px; overflow: hidden; }
  body {
    background: var(--stage);
    position: relative;
    font-family: "Josefin Sans", sans-serif;
  }
  .card {
    position: absolute;
    left: 399px;
    width: 409px;
    height: 237px;
    background: var(--card-light);
    overflow: hidden;
  }
  .card--front { top: 89px; }
  .card--back { top: 413px; height: 238px; }

  /* Front */
  .band { position: absolute; left: 0; width: 100%; background: var(--card-dark); }
  .band--top { top: 0; height: 66px; }
  .band--bottom { bottom: 0; height: 65px; }
  .contact-list { list-style: none; position: absolute; color: var(--text-on-dark); font-size: 9px; font-weight: 300; letter-spacing: 0.6px; white-space: nowrap; }
  .contact-list li { display: flex; align-items: center; }
  .contact-list svg { width: 9px; height: 9px; fill: var(--text-on-dark); flex: none; }
  .contact-list--phones { top: 11px; left: 296px; }
  .contact-list--phones li { height: 14px; gap: 16px; }
  .contact-list--address { top: 20px; left: 33px; }
  .contact-list--address li { height: 16px; gap: 4px; }
  .identity {
    position: absolute; top: 66px; left: 30px; height: 96px;
    display: flex; align-items: center; gap: 8px;
  }
  .identity__mark { display: flex; align-items: center; gap: 4px; font-family: "Cinzel", serif; font-weight: 600; font-size: 11px; color: var(--ink-soft); }
  .identity__mark .square { width: 9px; height: 9px; background: var(--ink-soft); }
  .identity__name { font-family: "Cinzel", serif; font-weight: 400; font-size: 23px; color: var(--ink); letter-spacing: 0.3px; }

  /* Back */
  .corner { position: absolute; width: 86px; height: 66px; background: var(--card-dark); }
  .corner--tl { top: 0; left: 0; }
  .corner--tr { top: 0; right: 0; }
  .corner--bl { bottom: 0; left: 0; }
  .corner--br { bottom: 0; right: 0; }
  .brand {
    position: absolute; top: 54px; left: 0; width: 100%;
    display: flex; flex-direction: column; align-items: center;
  }
  .brand__mark { display: flex; align-items: center; gap: 8px; font-family: "Cinzel", serif; font-weight: 600; font-size: 30px; color: var(--ink-soft); height: 113px; }
  .brand__mark .circle { width: 22px; height: 22px; border-radius: 50%; background: var(--ink-soft); }
  .brand__company { margin-top: 10px; font-family: "Cinzel", serif; font-weight: 600; font-size: 10.5px; color: var(--ink); letter-spacing: 0.2px; white-space: nowrap; }
</style>
</head>
<body>
  <section class="card card--front" aria-label="Business card front">
    <div class="band band--top">
      <ul class="contact-list contact-list--phones">
        <li><svg viewBox="0 0 10 10"><path d="M3 0h4a1 1 0 0 1 1 1v8a1 1 0 0 1-1 1H3a1 1 0 0 1-1-1V1a1 1 0 0 1 1-1zm0 1.5v6h4v-6z"/></svg>0400 555 182</li>
        <li><svg viewBox="0 0 10 10"><path d="M2.2 0.5l1.6 2-1 1.2c.7 1.4 1.8 2.5 3.2 3.2l1.2-1 2 1.6-1 1.8C4.5 9 1 5.5.5 1.5z"/></svg>(03) 9555 0147</li>
      </ul>
    </div>
    <div class="identity">
      <div class="identity__mark"><span class="square"></span>K&amp;R</div>
      <h1 class="identity__name">Owen Deloit</h1>
    </div>
    <div class="band band--bottom">
      <ul class="contact-list contact-list--address">
        <li><svg viewBox="0 0 10 10"><path d="M5 0a3.5 3.5 0 0 1 3.5 3.5C8.5 6 5 10 5 10S1.5 6 1.5 3.5A3.5 3.5 0 0 1 5 0zm0 2a1.5 1.5 0 1 0 0 3 1.5 1.5 0 0 0 0-3z"/></svg>P.O. Box 7 Ashgrove Victoria 3199</li>
        <li><svg viewBox="0 0 10 10"><path d="M0 2h10v6H0zm1 .8v.3l4 2.6 4-2.6v-.3z"/></svg>owen@krsecure.net.au / office@krsecure.net.au</li>
      </ul>
    </div>
  </section>

  <section class="card card--back" aria-label="Business card back">
    <div class="corner corner--tl"></div>
    <div class="corner corner--tr"></div>
    <div class="corner corner--bl"></div>
    <div class="corner corner--br"></div>
    <div class="brand">
      <div class="brand__mark"><span class="circle"></span>K&amp;R</div>
      <p class="brand__company">K&amp;R Security Services Pty. Ltd.</p>
    </div>
  </section>
</body>
</html>
```